" Empresa que trabalha com danças urbanas. Workhops, Batalhas, Performances, Palestras, Bate-papos, Jam Sessions. Também possui um projeto social em comunidades. "

```html
<!DOCTYPE html>
<html lang="pt-BR">
<head>
<meta charset="utf-8">
<title>Ginga Urbana Loja</title>
<link rel="stylesheet" href="https://fonts.googleapis.com/css2?family=Roboto+Condensed:wght@400;700&display=swap">
<style>
:root{
  --page-bg:#ffffff;
  --dark:#2a2a2a;
  --darker:#1c1c1c;
  --metal-light:#d6d6d6;
  --metal-mid:#a9a9a9;
  --lime:#b6c21a;
  --green:#6f8f1c;
  --yellow:#f2d21b;
  --card:#3a3a3a;
  --card-border:#555;
  --text-light:#eeeeee;
  --text-muted:#9a9a9a;
}
*{box-sizing:border-box;margin:0;padding:0}
html,body{width:1200px;height:1200px;overflow:hidden;background:var(--page-bg);font-family:"Roboto Condensed",sans-serif}
.site{position:absolute;left:187px;top:0;width:826px;height:1200px;background:repeating-linear-gradient(90deg,#2d2d2d 0 2px,#262626 2px 4px);}
.header{position:relative;height:108px;border-top:5px solid var(--lime);background:linear-gradient(180deg,#3b3b3b,#1f1f1f);}
.brand{position:absolute;left:36px;top:24px;display:flex;align-items:center;gap:10px;color:var(--text-light);font-weight:700;font-size:22px;line-height:1.05;width:170px}
.brand-mark{width:16px;height:16px;background:var(--lime);flex:none}
.account{position:absolute;right:33px;top:19px;width:140px;height:77px;background:linear-gradient(180deg,#5a5a5a,#3a3a3a);border:1px solid #666;padding:7px 8px}
.social{display:flex;gap:4px;justify-content:flex-end}
.social span{width:13px;height:13px;background:#ddd;border-radius:2px}
.account-link{display:flex;align-items:center;gap:7px;color:var(--text-light);font-size:11px;font-weight:700;margin-top:8px}
.account-link i{width:12px;height:12px;background:#ccc;border-radius:2px;display:block}
.nav{height:24px;background:linear-gradient(180deg,#ececec,var(--metal-mid));display:flex;justify-content:center;align-items:center;gap:15px}
.nav a{font-size:11px;color:#333;text-decoration:none}
.nav a.active{font-weight:700;color:#111}
.band{height:17px;background:linear-gradient(180deg,var(--yellow),var(--green))}
.hero{position:absolute;left:46px;top:185px;width:744px;height:255px;background:radial-gradient(ellipse at 50% 60%,#8a8a8a,#3c3c3c 45%,#050505 80%)}
.dots{position:absolute;left:0;right:0;top:446px;display:flex;justify-content:center;gap:5px}
.dots span{width:5px;height:5px;border-radius:50%;background:#ccc}
.dots span:first-child{background:var(--yellow)}
.products{position:absolute;left:34px;top:523px;display:grid;grid-template-columns:repeat(4,178px);column-gap:16px;row-gap:17px}
.card{height:222px;background:linear-gradient(180deg,var(--card),#2f2f2f);border:1px solid var(--card-border);text-align:center}
.card-img{height:156px;margin:4px}
.img-a{background:linear-gradient(135deg,#e9e9e9,#c23b3b 55%,#f0f0f0)}
.img-b{background:linear-gradient(135deg,#f2f2f2,#5b2a7a 40%,#6b3a8c)}
.img-c{background:linear-gradient(135deg,#f5f5f5,#1a1a1a 40%,#2b2b2b)}
.img-d{background:linear-gradient(135deg,#eaeaea,#8a7a52 40%,#5d4f36)}
.card h3{font-size:11px;font-weight:400;color:var(--text-light);margin-top:8px}
.price{font-size:17px;font-weight:700;color:var(--yellow);line-height:1.1}
.note{font-size:8px;color:var(--text-muted)}
.to-top{position:absolute;left:763px;top:1001px;width:30px;height:30px;background:#ddd;border-radius:3px}
.footer-bar{position:absolute;left:0;top:1044px;width:826px;height:24px;background:linear-gradient(180deg,#e5e5e5,#9c9c9c);display:flex;justify-content:center;align-items:center;gap:4px}
.footer-bar span{width:11px;height:11px;background:#333;border-radius:2px}
.footer{position:absolute;left:0;top:1075px;width:826px;height:125px;color:var(--text-light)}
.newsletter{position:absolute;left:33px;top:8px}
.footer h4{font-size:10px;font-weight:700;letter-spacing:.2px}
.news-form{display:flex;gap:4px;margin-top:6px}
.news-form span{width:132px;height:16px;background:#444;border:1px solid #666;font-size:8px;color:#999;padding:2px 4px}
.news-form b{width:20px;height:16px;background:#ccc;color:#222;font-size:9px;text-align:center;line-height:16px}
.widget{position:absolute;left:346px;top:0;width:144px;height:78px;background:#f2f2f2;border:1px solid #888}
.widget-photo{margin:24px 8px 0;height:40px;background:linear-gradient(90deg,#6d7b8f,#b59a7a,#5f6e55)}
.payments{position:absolute;right:33px;top:2px;text-align:right;font-size:8px;color:#ccc;line-height:1.35}
.payments h4{margin-bottom:3px}
.payments h4.spaced{margin-top:8px}
.copyright{position:absolute;left:0;right:0;top:108px;text-align:center;font-size:7px;color:var(--text-muted)}
</style>
</head>
<body>
<div class="site">
  <header class="header">
    <div class="brand"><span class="brand-mark"></span>Ginga Urbana Loja</div>
    <div class="account">
      <div class="social"><span></span><span></span><span></span><span></span><span></span></div>
      <div class="account-link"><i></i>MINHA CONTA</div>
      <div class="account-link"><i></i>MEU CARRINHO</div>
    </div>
  </header>
  <nav class="nav">
    <a>HOME</a><a class="active">T-SHIRTS</a><a>CALÇAS</a><a>CASACOS</a><a>BOTTONS</a><a>BLUSAS</a><a>EVENTOS</a><a>NEWS</a><a>QUEM SOMOS</a><a>CONTATO</a>
  </nav>
  <div class="band"></div>

  <div class="hero" role="img" aria-label="Foto de dançarinos de rua em roupas cinzas sobre fundo escuro"></div>
  <div class="dots"><span></span><span></span><span></span><span></span><span></span></div>

  <section class="products">
    <article class="card"><div class="card-img img-a" role="img" aria-label="Camiseta branca com estampa tipográfica vermelha e preta"></div><h3>T-SHIRT GINGA URBANA 2015</h3><p class="price">R$30,00</p><p class="note">parcele em até 3x</p></article>
    <article class="card"><div class="card-img img-b" role="img" aria-label="Camiseta roxa com estampa tipográfica"></div><h3>T-SHIRT GINGA URBANA 2015</h3><p class="price">R$30,00</p><p class="note">parcele em até 3x</p></article>
    <article class="card"><div class="card-img img-c" role="img" aria-label="Camiseta preta com ilustração de dançarino"></div><h3>T-SHIRT GINGA URBANA 2015</h3><p class="price">R$30,00</p><p class="note">parcele em até 3x</p></article>
    <article class="card"><div class="card-img img-d" role="img" aria-label="Camiseta com estampa total em tons marrons"></div><h3>T-SHIRT GINGA URBANA 2015</h3><p class="price">R$30,00</p><p class="note">parcele em até 3x</p></article>
    <article class="card"><div class="card-img img-c" role="img" aria-label="Camiseta preta com ilustração de dançarino"></div><h3>T-SHIRT GINGA URBANA 2015</h3><p class="price">R$30,00</p><p class="note">parcele em até 3x</p></article>
    <article class="card"><div class="card-img img-b" role="img" aria-label="Camiseta roxa com estampa tipográfica"></div><h3>T-SHIRT GINGA URBANA 2015</h3><p class="price">R$30,00</p><p class="note">parcele em até 3x</p></article>
    <article class="card"><div class="card-img img-c" role="img" aria-label="Camiseta preta com ilustração de dançarino"></div><h3>T-SHIRT GINGA URBANA 2015</h3><p class="price">R$30,00</p><p class="note">parcele em até 3x</p></article>
    <article class="card"><div class="card-img img-d" role="img" aria-label="Camiseta com estampa total em tons marrons"></div><h3>T-SHIRT GINGA URBANA 2015</h3><p class="price">R$30,00</p><p class="note">parcele em até 3x</p></article>
  </section>

  <div class="to-top"><svg width="30" height="30" viewBox="0 0 30 30"><path d="M9 18l6-6 6 6" fill="none" stroke="#333" stroke-width="2.5"/></svg></div>

  <div class="footer-bar"><span></span><span></span><span></span><span></span></div>
  <footer class="footer">
    <div class="newsletter">
      <h4>RECEBA NOSSAS NOVIDADES</h4>
      <div class="news-form"><span>Digite seu e-mail</span><b>OK</b></div>
    </div>
    <div class="widget"><div class="widget-photo" role="img" aria-label="Mosaico de fotos de seguidores da página"></div></div>
    <div class="payments">
      <h4>MEIOS DE PAGAMENTO</h4>
      <p>BOLETO</p><p>CARTÃO</p>
      <h4 class="spaced">SOBRE NÓS</h4>
      <p>QUEM SOMOS</p><p>CONTATO</p>
    </div>
    <p class="copyright">© 2015 Ginga Urbana Loja · Todos os direitos reservados</p>
  </footer>
</div>
</body>
</html>
```